adult dating promotion banners

target website: zomerlantaarnbos.nl
i need multiple good banner for an add campaign on plovix.net
no male images in the banner, onlygirls
animatedly: yes
sizes: 300x250px and 728x110px

Target Market(s)

dutch guys looking for an date

Industry/Entity Type

dating

Requirements
Must have
• striking pictures
Nice to have
• free signup 2 free credits
Should not have
• no male images

```html
<!DOCTYPE html>
<html lang="en">
<head>
<meta charset="utf-8">
<title>Free Signup – Banner Set</title>
<link href="https://fonts.googleapis.com/css2?family=Inter:wght@700;800;900&family=Roboto+Condensed:wght@700&family=Montserrat:wght@200&display=swap" rel="stylesheet">
<style>
  :root {
    --canvas: #ffffff;
    --orange-deep: #ff7a00;
    --orange: #ff9800;
    --amber: #ffb400;
    --yellow: #ffd21f;
    --pill-light: #ffe066;
    --pill-dark: #ffbf1a;
    --cta-top: #ffa21a;
    --cta-bottom: #f07000;
    --white: #ffffff;
    --ink: #111111;
    --frame: #000000;
    --label: #f39a2b;
    --skin: #e9b896;
    --hair: #5a3a26;
  }
  * { box-sizing: border-box; margin: 0; padding: 0; }
  html, body { width: 1200px; height: 876px; overflow: hidden; background: var(--canvas); }
  .board { position: relative; width: 1200px; height: 876px; }

  .banner {
    position: absolute;
    overflow: hidden;
    border: 1px solid var(--frame);
    background: linear-gradient(125deg, var(--orange-deep) 0%, var(--orange) 35%, var(--amber) 65%, var(--yellow) 100%);
  }
  .banner-square { left: 151px; top: 100px; width: 375px; height: 312px; }
  .banner-leader { left: 151px; top: 554px; width: 910px; height: 137px;
    background: linear-gradient(110deg, var(--orange-deep) 0%, var(--amber) 40%, var(--yellow) 60%, var(--orange) 85%, var(--orange-deep) 100%); }

  .decor { position: absolute; inset: 0; width: 100%; height: 100%; }

  .model-photo {
    position: absolute;
    background: radial-gradient(ellipse at 45% 40%, var(--skin) 0%, #d49a74 38%, var(--hair) 70%, rgba(90,58,38,0) 100%);
  }
  .banner-square .model-photo { left: 150px; top: 0; width: 225px; height: 312px; }
  .banner-leader .model-photo { left: 20px; top: 0; width: 200px; height: 137px; }

  .headline {
    position: absolute;
    font-family: "Inter", Arial, sans-serif;
    font-weight: 900;
    color: var(--white);
    line-height: 0.92;
    text-align: center;
    letter-spacing: -0.5px;
    text-shadow: 0 2px 4px rgba(150,60,0,0.35);
  }
  .headline .line-big { display: block; }
  .headline .line-small { display: block; }
  .banner-square .headline { left: 16px; top: 76px; width: 142px; }
  .banner-square .line-big { font-size: 50px; }
  .banner-square .line-small { font-size: 31px; }
  .banner-leader .headline { left: 505px; top: 20px; width: 196px; }
  .banner-leader .line-big { font-size: 64px; }
  .banner-leader .line-small { font-size: 41px; }

  .credit-pill {
    position: absolute;
    display: flex; align-items: center; justify-content: center;
    border-radius: 999px;
    background: linear-gradient(180deg, var(--pill-light), var(--pill-dark));
    font-family: "Roboto Condensed", "Arial Narrow", sans-serif;
    font-weight: 700;
    color: var(--ink);
    box-shadow: 0 2px 4px rgba(160,70,0,0.3);
  }
  .banner-square .credit-pill { left: 19px; top: 162px; width: 190px; height: 37px; font-size: 20px; }
  .banner-leader .credit-pill { left: 221px; top: 52px; width: 280px; height: 50px; font-size: 26px; }

  .cta-button {
    position: absolute;
    display: flex; align-items: center; justify-content: center;
    border-radius: 999px;
    background: linear-gradient(180deg, var(--cta-top), var(--cta-bottom));
    border: 2px solid rgba(255,220,140,0.7);
    font-family: "Inter", Arial, sans-serif;
    font-weight: 800;
    color: var(--white);
    box-shadow: 0 2px 5px rgba(140,50,0,0.35);
  }
  .banner-square .cta-button { left: 39px; top: 255px; width: 117px; height: 35px; font-size: 14px; }
  .banner-leader .cta-button { left: 759px; top: 81px; width: 117px; height: 35px; font-size: 14px; }

  .scroll-cue { position: absolute; left: 809px; top: 22px; width: 30px; height: 32px; }

  .draft-label {
    position: absolute;
    right: 75px; top: 208px;
    font-family: "Montserrat", Arial, sans-serif;
    font-weight: 200;
    font-size: 48px;
    line-height: 1.1;
    letter-spacing: 3px;
    color: var(--label);
    text-align: right;
  }
</style>
</head>
<body>
<main class="board">

  <section class="banner banner-square" aria-label="300 by 250 banner">
    <svg class="decor" viewBox="0 0 375 312" aria-hidden="true">
      <circle cx="20" cy="160" r="120" fill="#ffffff" opacity="0.06"/>
      <circle cx="330" cy="5" r="30" fill="#ff7a00" opacity="0.5"/>
      <path d="M0 312 L120 180 L190 312 Z" fill="#ffcf2e" opacity="0.35"/>
    </svg>
    <div class="model-photo" role="img" aria-label="Photo of a smiling young woman with long brown hair, hand at her cheek"></div>
    <h2 class="headline"><span class="line-big">FREE</span><span class="line-small">SIGNUP</span></h2>
    <p class="credit-pill">$2 FREE CREDITS</p>
    <p class="cta-button">CLICK HERE</p>
  </section>

  <p class="draft-label">DRAFT<br>GIF ANIMATED</p>

  <section class="banner banner-leader" aria-label="728 by 110 banner">
    <svg class="decor" viewBox="0 0 910 137" aria-hidden="true">
      <path d="M250 137 L370 0 L470 0 L350 137 Z" fill="#ffffff" opacity="0.07"/>
      <path d="M560 137 L680 0 L740 0 L620 137 Z" fill="#ffffff" opacity="0.06"/>
      <circle cx="470" cy="150" r="60" fill="none" stroke="#ff7a00" stroke-width="14" opacity="0.35"/>
      <circle cx="890" cy="10" r="40" fill="#ff6a00" opacity="0.4"/>
    </svg>
    <div class="model-photo" role="img" aria-label="Photo of a young woman with long brown hair, hand raised to her face"></div>
    <p class="credit-pill">$2 FREE CREDITS</p>
    <h2 class="headline"><span class="line-big">FREE</span><span class="line-small">SIGNUP</span></h2>
    <svg class="scroll-cue" viewBox="0 0 30 32" aria-hidden="true">
      <path d="M3 3 L15 13 L27 3" fill="none" stroke="#ffffff" stroke-width="5" stroke-linejoin="miter"/>
      <path d="M3 17 L15 27 L27 17" fill="none" stroke="#ffffff" stroke-width="5" stroke-linejoin="miter"/>
    </svg>
    <p class="cta-button">CLICK HERE</p>
  </section>

</main>
</body>
</html>
```